Wine Tasting Event

We need a flyer design for a wine tasting event on Friday, February 14th. This is NOT a Valentine's themed event. It's merely an event for both singles and couples who do not want to drop a ton of money on a traditional meal at a fine restaurant. There will be good wines to taste, light snacks, info sessions on how to taste/appreciate good wine, live music, and a full bar in addition to the wine.

The event is called "Poured by the Greenway" and will be held at a venue overlooking the beautiful Marrow Creek Trail path.

We had an initial idea of a Large Wine cork taking up the majority of the flyer, with all of the information printed on it (as if it were a part of the cork). We are not designers, but have attached the initial attempt at the idea. Warning - It's bad.

Target Market(s)

Men and Women aged 21-35.

Industry/Entity Type

Restaurant

Requirements
Must have
• Name: Poured by the Greenway
Date: Friday, February 14th
Logo: Dunmore Leisure and Games League (See Attached File)

*NOTE Logo should not be a focal point of design. Just needs to be somewhere on the flyer. Can be substituted fo "Dunmore Leisure and Games League Presents"

Needs to be adaptable for 4"x6", 8.5"x11", and 11"x17"
Nice to have
• Wine cork, bottle, or glass. Something Atlanta related, or related to the Marrow Creek Trail.
Should not have
• Anything related to Valentine's Day

```html
<!DOCTYPE html>
<html lang="en">
<head>
<meta charset="utf-8">
<title>Poured by the Greenway — Flyer</title>
<link rel="stylesheet" href="https://fonts.googleapis.com/css2?family=Great+Vibes&family=Oswald:wght@300;400&family=Roboto+Condensed:wght@300&display=swap">
<style>
  :root {
    --backdrop: #5e0e10;
    --flyer-top: #5a1012;
    --flyer-mid: #3a0a0b;
    --flyer-bottom: #0c0303;
    --bottle-light: #5a4a46;
    --bottle-dark: #1e1414;
    --glass-light: #e8322e;
    --glass-dark: #7a0e10;
    --grape-light: #4a2a2e;
    --grape-dark: #140a0c;
    --gold-light: #ffd63a;
    --gold-deep: #d3961a;
    --league-red: #e3242b;
    --date-white: #f4f1ee;
  }
  * { margin: 0; padding: 0; box-sizing: border-box; }
  html, body {
    width: 1000px;
    height: 1200px;
    overflow: hidden;
    background: var(--backdrop);
  }
  .canvas {
    position: relative;
    width: 1000px;
    height: 1200px;
    background: radial-gradient(ellipse at 50% 45%, #6e1214 0%, var(--backdrop) 70%);
  }
  .flyer {
    position: absolute;
    left: 218px;
    top: 127px;
    width: 610px;
    height: 913px;
    overflow: hidden;
    background: linear-gradient(180deg, var(--flyer-top) 0%, var(--flyer-mid) 60%, var(--flyer-bottom) 100%);
    box-shadow: 0 20px 50px rgba(0,0,0,0.55);
  }
  .bottle-art {
    position: absolute;
    left: 134px;
    top: 43px;
    width: 196px;
    height: 800px;
    border-radius: 60px 60px 8px 8px;
    background: linear-gradient(180deg, var(--bottle-light) 0%, var(--bottle-dark) 100%);
    opacity: 0.9;
  }
  .glass-art {
    position: absolute;
    left: 272px;
    top: 243px;
    width: 222px;
    height: 640px;
    border-radius: 20px 20px 110px 110px / 20px 20px 60px 60px;
    background: linear-gradient(180deg, rgba(232,50,46,0.35) 0%, var(--glass-light) 35%, var(--glass-dark) 60%, rgba(40,8,8,0.6) 100%);
  }
  .grapes-art {
    position: absolute;
    left: 34px;
    top: 688px;
    width: 190px;
    height: 200px;
    border-radius: 50% 50% 45% 45%;
    background: radial-gradient(ellipse at 50% 40%, var(--grape-light) 0%, var(--grape-dark) 100%);
  }
  .league-mark {
    position: absolute;
    right: 50px;
    top: 100px;
    width: 220px;
    text-align: right;
    font-family: "Oswald", sans-serif;
    font-weight: 400;
    font-size: 15px;
    line-height: 1.15;
    letter-spacing: 0.06em;
    text-transform: uppercase;
    color: var(--league-red);
  }
  .title {
    position: absolute;
    left: 0;
    top: 560px;
    width: 565px;
    text-align: center;
  }
  .gold {
    background: linear-gradient(180deg, var(--gold-light) 0%, var(--gold-deep) 100%);
    -webkit-background-clip: text;
    background-clip: text;
    color: transparent;
  }
  .title-script {
    display: block;
    font-family: "Great Vibes", cursive;
    font-size: 122px;
    line-height: 1;
  }
  .title-connector {
    display: block;
    margin-top: 0;
    font-family: "Oswald", sans-serif;
    font-weight: 400;
    font-size: 19px;
    letter-spacing: 0.32em;
    color: var(--gold-light);
  }
  .title-place {
    display: block;
    margin-top: -4px;
    font-family: "Oswald", sans-serif;
    font-weight: 300;
    font-size: 82px;
    line-height: 1;
    letter-spacing: 0.02em;
  }
  .flourish {
    position: absolute;
    left: 240px;
    top: 804px;
    width: 68px;
    height: 12px;
    border-radius: 6px;
    background: linear-gradient(90deg, rgba(211,150,26,0.2), var(--gold-light), rgba(211,150,26,0.2));
  }
  .event-date {
    position: absolute;
    left: 0;
    top: 826px;
    width: 555px;
    text-align: center;
    font-family: "Roboto Condensed", sans-serif;
    font-weight: 300;
    font-size: 28px;
    color: var(--date-white);
  }
</style>
</head>
<body>
  <main class="canvas">
    <section class="flyer">
      <div class="bottle-art" role="img" aria-label="Dark wine bottle whose body reflects the Marrow Creek Trail at dusk"></div>
      <div class="glass-art" role="img" aria-label="Tall stemmed glass half filled with red wine"></div>
      <div class="grapes-art" role="img" aria-label="Bunch of dark red grapes"></div>

      <p class="league-mark">Dunmore Leisure<br>and Games League</p>

      <h1 class="title">
        <span class="title-script gold">Poured</span>
        <span class="title-connector">BY THE</span>
        <span class="title-place gold">GREENWAY</span>
      </h1>

      <div class="flourish" role="img" aria-label="Small gold scroll ornament"></div>

      <p class="event-date">Friday, February 14th</p>
    </section>
  </main>
</body>
</html>
```